Social Media Beitrag (Stelle)
Alles perfekt, sehr unkomplizierte Zusammenarbeit. Schnell ein passendes Design gefunden. Die Vorstellungen wurden super entgegengenommen und umgesetzt.
Zielgruppe
Wir sind eine allgemeinmedizinischen Tierklinik, welche Unterstützung im Team sucht. Aus diesem Grund ist die Zielgruppe bei dieser Arbeit potentielle Mitarbeiter.
Aufgabenstellung
Wir möchten gerne einen Social-Media-Beitrag beispielsweise auf Pixelbrunn und Kontaktwand machen und deshalb das Stelleninserat (im Anhang) in anderer verkürzter ansprechender Art darstellen. Ich stelle mir vor die Message auf ca. 3-4 quadratischen Bilder darzustellen, dass der Leser diese nacheinander ansehen kann und direkt angesprochen wird. Es muss nicht alles vom Stelleninserat mit eingebaut werden, sondern nur das wichtigste. Bei Pixelbrunn wäre ideale Größe für quadratische Posts ist 1080 px x 1080 px mit einem Seitenverhältnis von 1:1. Wir sind jedoch für andere Ideen offen oder wenn ihr auch das Gefühl habt wir packen die Message auf ein Bild. Ziel ist es möglichst ein breites Publikum online ansprechen zu können. Das Corporate Design der Unternehmung sollte auch mit berücksichtigt werden. Das Design sollte im Indesign oder Photoshop erstellt werden, damit wir es selbständig überarbeiten oder erweitern können.
Ich möchte keine BildVorrat-Personen auf den Post abbilden, dass wirkt zu künstlich, da es nicht die richtigen Mitarbeiter sind. Vielleicht kann auch etwas mit wenig Bild oder gar kein Bild und einfach einem Icon dargestellt werden.

```html
<!DOCTYPE html>
<html lang="de">
<head>
<meta charset="utf-8">
<title>Talmatt Tierarzt – Stelle Empfang TPA</title>
<link rel="stylesheet" href="https://fonts.googleapis.com/css2?family=Josefin+Sans:wght@400;700&family=Kaushan+Script&family=Roboto+Condensed:wght@700&display=swap">
<style>
  :root {
    --brand-red: #c8003c;
    --text-grey: #7b7b7b;
    --heart-pink: #f6dde3;
    --paper: #ffffff;
  }
  html, body {
    margin: 0;
    padding: 0;
    width: 1200px;
    height: 1200px;
    overflow: hidden;
    background: var(--paper);
  }
  .post {
    position: relative;
    width: 1200px;
    height: 1200px;
    overflow: hidden;
    background: var(--paper);
  }
  .heart-decor {
    position: absolute;
    left: 805px;
    top: 780px;
    width: 420px;
    height: 420px;
  }
  .photo {
    position: absolute;
    top: 0;
  }
  .photo--dog-curly {
    left: 0;
    width: 398px;
    height: 457px;
    background: radial-gradient(circle at 45% 50%, #c98a52 0%, #d9a473 45%, #ece3da 100%);
  }
  .photo--cat {
    left: 400px;
    width: 397px;
    height: 457px;
    background: radial-gradient(circle at 50% 55%, #f4f1f2 0%, #e3b9c6 55%, #e596ad 100%);
  }
  .photo--cat-paws {
    position: absolute;
    top: 440px;
    left: 402px;
    width: 393px;
    height: 80px;
    border-radius: 0 0 40px 40px;
    background: linear-gradient(180deg, #e7a7ba 0%, #f2e9ec 100%);
  }
  .photo--dog-terrier {
    left: 800px;
    width: 400px;
    height: 457px;
    background: radial-gradient(circle at 50% 45%, #3a2b24 0%, #8b5a34 40%, #f4e6de 100%);
  }
  .brand {
    position: absolute;
    left: 41px;
    top: 530px;
    margin: 0;
    font-family: "Josefin Sans", sans-serif;
    font-weight: 400;
    font-size: 60px;
    letter-spacing: 2px;
    text-transform: uppercase;
    color: var(--brand-red);
    line-height: 1;
  }
  .headline {
    position: absolute;
    left: 0;
    top: 620px;
    width: 1200px;
    margin: 0;
    font-family: "Kaushan Script", cursive;
    font-weight: 400;
    color: var(--brand-red);
    text-align: center;
    line-height: 1;
  }
  .headline__line {
    display: block;
    font-size: 142px;
  }
  .headline__line--first {
    margin-left: -10px;
  }
  .headline__line--second {
    margin-top: 34px;
    font-size: 152px;
  }
  .position {
    position: absolute;
    left: 40px;
    top: 1128px;
    margin: 0;
    font-family: "Josefin Sans", sans-serif;
    font-weight: 400;
    font-size: 52px;
    letter-spacing: 3px;
    text-transform: uppercase;
    color: var(--text-grey);
    line-height: 1;
    white-space: nowrap;
  }
  .position__share {
    font-family: "Roboto Condensed", sans-serif;
    font-weight: 700;
    letter-spacing: 0;
  }
</style>
</head>
<body>
  <main class="post">
    <svg class="heart-decor" viewBox="0 0 420 420" aria-hidden="true">
      <path d="M210 395 L40 220 C-10 165 5 70 80 50 C135 35 180 65 210 100 C240 65 285 35 340 50 C415 70 430 165 380 220 Z"
            fill="none" stroke="var(--heart-pink)" stroke-width="22" stroke-linejoin="round"/>
    </svg>

    <div class="photo photo--dog-curly" role="img" aria-label="Foto eines rotbraunen, lockigen Hundes mit herausgestreckter Zunge"></div>
    <div class="photo photo--cat" role="img" aria-label="Foto einer schwarz-weissen Katze vor rosa Hintergrund"></div>
    <div class="photo--cat-paws" role="img" aria-label="Die weissen Pfoten der Katze ragen über den Bildrand"></div>
    <div class="photo photo--dog-terrier" role="img" aria-label="Foto eines dreifarbigen Terriers mit abstehenden Ohren"></div>

    <p class="brand">Talmatt Tierarzt</p>

    <h1 class="headline">
      <span class="headline__line headline__line--first">Sucht Helfer mit</span>
      <span class="headline__line headline__line--second">Herz und Verstand</span>
    </h1>

    <p class="position">Mitarbeiter/in Empfang TPA <span class="position__share">(80-100%)</span></p>
  </main>
</body>
</html>
```